Relaunch of company website (Technical company)

Hi all,

we need a website based on Wordpress who makes the customer curious and excited of all the possibilities we can offer.
Customers are B2B. The layout should be based on the screenshots I added, but refreshed and modernized with some nice gadgets.
All needs to be responsive for the different devices.
We are a technical company. We provide a full range of service from 3D scan, Manufacturing, Prototyping, Bulk production and CAD service.

Later the website needs to have a multi language option.

Home:

1. Logo top left (attached)
2. Menu bar top right
3. Header picture like in the screenshot
4. Than the three small blue pics (CAD - Fertigung - Manufaktur) we want a
hoover-small zoom effect as soon as the mouse hits them.
5. Introduction text of our company
6. Contact Information (Design sample see attachment)
7. At the end "Impressum - Datenschutzerklärung - Haftungsausschluss. Those need to be linked to extra pages where we can add mandatory text (Legal notice, Privacy, Disclaimer)

Leistungen - Our service:

1. See the attachment named our service.
2. First on page a gallery where we can add pictures. If moving the mouse over the picture we want a one line explanation e.g. 3D Scan, Production, Die cast...
no click option at the pictures, just to see.
3. Below that, a side menu (we need to add or remove items by our self if necessary) on the left where we can add our service.
4. If the customer is clicking a service, it needs to be highlighted
5. After clicking a service we want our text to that service appear right of the menu (see attachment sample) and 2 big pictures on top of the menu and text field.

Gallery:

1. Headline pictures for each gallery Category (6-8 at the moment)
2. Mouse over the picture zooms it a little in and adds a text what category it is
e.g. Reverse engineering, Prototyping, Laserscan
3. Clicking on the picture opens the detail gallery to that category. There we need
to add pictures specific to that service.
4. If the customer is clicking on a picture from there, all pictures from that
Category will open in a full screen view mode

Blog:

1. A blog to add news (picture and text). Right now we don´t have the time to feed
it, so we want to deactivate it as long as we cant keep it up to date. Later it
should be part of the website.

Unternehmen:

1. Drop down menu: Our Team - History - Unsere Partner - AGB - Impressum

Our Team:
1. Short description of our employees including picture (see attachment)
2. Contact Information (Design sample see attachment)
3. At the end "Impressum - Datenschutzerklärung - Haftungsausschluss. Those need to be linked to extra pages where we can add mandatory text (Legal notice, Privacy, Disclaimer)

History:
1. Timeline where we can add milestones including date, and pictures of the company (see screenshot)

Unsere Partner:
1. Text field where we can introduce our partners including pictures if necessary.

A blog would be a nice option, social media shortcuts to Glimorra-KL but no preview of KL Timeline within the website.

We do have professional text already, that will be added by us. We expect you to use any sample text and pictures for the draft, beside what we supply already.

If you see the need of buying pictures from Velto or any other picture company that is OK for us.

What we expect:

A modern, fresh website based on our existing design, changes are fine as long as the whole website design does not change completely to an unicorn thing in pink. Feel free to be creative. New ideas will be discussed, we are open to good ideas. We don´t stick fix to our idea, but we want our customers can see that its still the same company.
Scrolling effects would be a nice gadget if possible.

We have a bad page already...don´t want a second bad one :-)

Our company blue is RBG 106, 206, 224

Greets to all, looking for professional results.

Target Market(s)

B2B, Engineering companys,

Industry/Entity Type

Technical Service

Number of Pages Required

5+ page

Font styles to use
Sans Serif
Other font styles liked:
• verdana

Colors
0455a3
000000
ffffff

Requirements
Must have
• Responsive design, We want to be able to add posts to the Blog, pictures to the categories, and categories by ourself if necessary. (Wordpress)
• Lets say we want to add one more category at „Leistungen-Our Service“ that should be possible for us in the wordpress background.
Nice to have
• Dynamic elements to make the website more alive.
Should not have
• Sliders, Contact form

```html
<!DOCTYPE html>
<html lang="de">
<head>
<meta charset="utf-8">
<title>Ostrel Precision</title>
<link href="https://fonts.googleapis.com/css2?family=Cinzel:wght@400;700&family=Open+Sans:wght@300;400;600;700&display=swap" rel="stylesheet">
<style>
:root{
  --ink:#1a1a1a;
  --hero-dark:#0f5482;
  --hero-mid:#1f6f9f;
  --band:#36a8e6;
  --band-light:#44b7f3;
  --footer:#2c2c2c;
  --footer-bar:#3a3a3a;
  --muted:#555;
  --white:#fff;
}
*{margin:0;padding:0;box-sizing:border-box}
html,body{width:807px;height:1200px;overflow:hidden;background:#fff}
body{position:relative;font-family:"Open Sans",Verdana,sans-serif;color:var(--ink)}
.abs{position:absolute}
.serif{font-family:"Cinzel",serif;font-weight:400}

/* header */
.site-header{left:0;top:0;width:807px;height:55px;background:#fff;border-bottom:1px solid #ddd}
.logo{left:110px;top:16px;font-size:19px;font-weight:300;letter-spacing:.3px;color:var(--ink)}
.topline{top:12px;left:583px;font-size:7px;color:#444}
.lang{top:12px;left:677px;font-size:7px;color:#444}
.lang::after{content:"";display:inline-block;margin-left:4px;border:3px solid transparent;border-top:4px solid var(--band);vertical-align:-2px}
.main-nav{top:28px;left:471px;display:flex;gap:13px;font-size:10.5px;font-weight:600;color:#222}

/* hero */
.hero{left:0;top:55px;width:807px;height:321px;background:linear-gradient(135deg,var(--hero-mid) 0%,#1c77a6 45%,var(--hero-dark) 100%)}
.hero-title{left:125px;top:96px;font-size:31px;line-height:34px;color:#fff;font-variant:small-caps;letter-spacing:.5px}
.hero-text{left:125px;top:178px;width:250px;font-size:9px;line-height:11px;color:#fff}
.hero-arrow{top:145px}
.hero-media{border-radius:40px;background:radial-gradient(circle,#c9ced3 0%,#6b7075 55%,rgba(40,60,80,0) 75%)}

/* features */
.features{left:0;top:376px;width:807px;height:128px;background:var(--band)}
.feature-active{left:277px;top:4px;width:253px;height:129px;background:var(--band-light)}
.feature{color:#fff}
.feature h3{font-size:10.5px;font-weight:700;margin-bottom:5px;letter-spacing:.3px}
.feature p{font-size:7.5px;line-height:9.5px;width:112px}

/* about */
.about-photo{left:406px;top:549px;width:343px;height:261px;background:linear-gradient(135deg,#3b3b3b 0%,#9a9a9a 40%,#d0d0d0 60%,#2a2a2a 100%);clip-path:polygon(20% 0,100% 0,100% 100%,0 100%)}
.about-box{left:108px;top:566px;width:411px;height:228px;background:var(--band-light);color:#fff;padding:14px 26px 0 33px}
.about-box h2{font-size:25px;font-variant:small-caps;line-height:28px}
.about-box .lead{font-size:8.5px;font-weight:700;line-height:12px;margin-bottom:10px}
.about-box p{font-size:8.3px;line-height:10.3px;text-align:justify}
.about-box p+p{margin-top:10px}

/* intro */
.divider{left:0;top:826px;width:807px;height:3px;background:linear-gradient(#e6e6e6,#fff)}
.intro-title{left:0;top:856px;width:807px;text-align:center;font-size:27px;font-variant:small-caps;letter-spacing:.5px}
.intro-text{left:189px;top:905px;width:430px;text-align:center;font-size:8.4px;line-height:10.5px;color:var(--muted)}

/* footer */
.site-footer{left:0;top:980px;width:807px;height:186px;background:var(--footer);color:#ddd}
.footer-logo{left:110px;top:47px;font-size:22px;font-weight:300;line-height:26px;color:#fff}
.social{top:122px;left:108px;display:flex;gap:7px}
.social span{width:13px;height:13px;border:1px solid #ccc;border-radius:50%}
.col h4{font-size:9px;font-weight:400;color:#fff;margin-bottom:9px}
.col li{list-style:none;font-size:8px;line-height:15.2px}
.col li.strong{font-weight:600;font-size:8.8px;color:#fff}
.col p{font-size:7.5px;line-height:10px}
.email-field{left:538px;top:99px;width:162px;height:18px;background:#fff;font-size:7px;color:#333;padding:5px 0 0 28px}
.email-field svg{position:absolute;left:9px;top:5px}
.submit{left:538px;top:123px;width:61px;height:17px;background:var(--band);color:#fff;font-size:7.5px;text-align:center;line-height:17px}
.footer-bar{left:0;top:1166px;width:807px;height:34px;background:var(--footer-bar);color:#ddd;font-size:7.2px;text-align:center;line-height:34px}
</style>
</head>
<body>

<header class="abs site-header">
  <div class="abs logo">OSTREL PRECISION</div>
  <div class="abs topline">phone: (000) 000-0000</div>
  <div class="abs lang">EN</div>
  <nav class="abs main-nav"><span>Home</span><span>Leistungen</span><span>Galerie</span><span>Unternehmen</span></nav>
</header>

<section class="abs hero">
  <h1 class="abs hero-title serif">Welcome!<br>Ostrel Precision</h1>
  <p class="abs hero-text">Lorem Ipsum is simply dummy text of the printing and typesetting industry. Lorem Ipsum has been the industry's standard dummy text ever since</p>
  <svg class="abs hero-arrow" style="left:53px" width="16" height="28" viewBox="0 0 16 28"><polyline points="14,2 2,14 14,26" fill="none" stroke="#8fc7e8" stroke-width="2"/></svg>
  <svg class="abs hero-arrow" style="left:742px" width="16" height="28" viewBox="0 0 16 28"><polyline points="2,2 14,14 2,26" fill="none" stroke="#3fc0ff" stroke-width="2"/></svg>
  <div class="abs hero-media" style="left:395px;top:67px;width:150px;height:140px" role="img" aria-label="Machined steel gear coupling"></div>
  <div class="abs hero-media" style="left:565px;top:137px;width:160px;height:133px" role="img" aria-label="Precision-machined pump housing"></div>
</section>

<section class="abs features">
  <div class="abs feature-active"></div>
  <svg class="abs" style="left:94px;top:40px" width="50" height="52" viewBox="0 0 50 52" fill="none" stroke="#fff" stroke-width="4" stroke-linejoin="round"><polygon points="25,3 47,14 47,38 25,49 3,38 3,14"/><polyline points="3,14 25,25 47,14"/><line x1="25" y1="25" x2="25" y2="49"/></svg>
  <div class="abs feature" style="left:155px;top:43px"><h3>CAD SERVICE</h3><p>Lorem Ipsum is simply dummy text of the printing and type setting industry.</p></div>
  <svg class="abs" style="left:330px;top:38px" width="44" height="56" viewBox="0 0 44 56" fill="none" stroke="#fff" stroke-width="3.5"><path d="M22 3 L41 9 V30 C41 42 32 50 22 53 C12 50 3 42 3 30 V9 Z"/><rect x="12" y="22" width="20" height="12" rx="3" fill="#fff" stroke="none"/><rect x="16" y="25" width="4" height="2.5" fill="var(--band-light)" stroke="none"/><rect x="24" y="25" width="4" height="2.5" fill="var(--band-light)" stroke="none"/><rect x="16" y="29" width="12" height="2.5" fill="var(--band-light)" stroke="none"/></svg>
  <div class="abs feature" style="left:393px;top:41px"><h3>FERTIGUNG</h3><p>Lorem Ipsum is simply dummy text of the printing and type setting industry.</p></div>
  <svg class="abs" style="left:540px;top:38px" width="44" height="54" viewBox="0 0 44 54" fill="#fff"><rect x="34" y="2" width="8" height="30"/><polygon points="2,54 2,32 12,24 12,32 22,24 22,32 32,24 32,32 42,32 42,54 24,54 24,44 14,44 14,54"/><rect x="5" y="38" width="14" height="3" fill="var(--band)"/></svg>
  <div class="abs feature" style="left:591px;top:43px"><h3>MANUFAKTUR</h3><p>Lorem Ipsum is simply dummy text of the printing and type setting industry.</p></div>
</section>

<section>
  <div class="abs about-photo" role="img" aria-label="CNC milling tool cutting an aluminium block"></div>
  <div class="abs about-box">
    <h2 class="serif">About Ostrel Precision</h2>
    <p class="lead">Neque porro quisquam est qui dolorem ipsum quia dolor sit amet,<br>consectetur, adipisci velit.</p>
    <p>Lorem Ipsum is simply dummy text of the printing and typesetting industry. Lorem Ipsum has been the industry's standard dummy text ever since the 1500s, when an unknown printer took a galley of type and scrambled it to make a type specimen book. It has survived not only five centuries, but also the leap into electronic typesetting, remaining essentially unchanged. It was popularised in the 1960s with the release of Sheetwell sheets containing Lorem Ipsum passages, and more recently with desktop publishing software like Pagewright Studio including versions of Lorem Ipsum.</p>
    <p>Why do we use it?<br>It is a long established fact that a reader will be distracted by the readable content of a page when looking at its layout. The point of using Lorem Ipsum is that it has a more-or-less normal distribution of letters, as opposed to using 'Content here, content here</p>
  </div>
</section>

<div class="abs divider"></div>
<section>
  <h2 class="abs intro-title serif">Finibus Bonorum et Malorum</h2>
  <p class="abs intro-text">Sed ut perspiciatis unde omnis iste natus error sit voluptatem accusantium doloremque laudantium, totam rem aperiam, eaque ipsa quae ab illo inventore veritatis et quasi architecto beatae vitae dicta sunt explicabo.<br>Nemo enim ipsam voluptatem quia voluptas sit aspernatur aut odit aut fugit,</p>
</section>

<footer class="abs site-footer">
  <div class="abs footer-logo">OSTREL<br>PRECISION</div>
  <div class="abs social"><span></span><span></span><span></span><span></span></div>
  <div class="abs col" style="left:280px;top:46px">
    <h4>Conact us</h4>
    <ul><li class="strong">Ostrel Precision</li><li class="strong">Corporate Office</li><li>P.O. Box 0 OP, Ostrelfeld 99566</li><li>info@ostrel-mail.de</li><li>Phone: 000 000 0000</li><li>Fax: 000 000 0000</li></ul>
  </div>
  <div class="abs col" style="left:438px;top:47px">
    <h4>Discover</h4>
    <ul><li>Impressum</li><li>Datenschutzerklärung</li><li>Haftungsausschluss</li></ul>
  </div>
  <div class="abs col" style="left:538px;top:46px">
    <h4>Subscribe with us</h4>
    <p>Sign up for our mailing list to get latest<br>updates and offers</p>
  </div>
  <div class="abs email-field"><svg width="11" height="8" viewBox="0 0 11 8" fill="none" stroke="#333" stroke-width="1"><rect x=".5" y=".5" width="10" height="7"/><polyline points=".5,.5 5.5,4.5 10.5,.5"/></svg>Email Address</div>
  <div class="abs submit">Submit</div>
</footer>
<div class="abs footer-bar">© 2006–2018 website, All rights reserved &nbsp;|&nbsp; Legal notice &nbsp;|&nbsp; Privacy &nbsp;|&nbsp; Disclaimer</div>

</body>
</html>
```